Cedar Hollow at Pine Basin Marketing Sign

I need a sign designed that will be 4'X8'. You designed another sign for me not too long ago - Fernridge at Harlow's Point. I need another sign similar in layout, but with the Cedar Hollow logo, tagline, rendering, colors, etc.

Attached is the logo, and rendering. Here are the other items I need to have on this sign:
Tagline - Life Outside The Lines
JOIN OUR WAITLIST TODAY!
Move-In Beginning Summer 2017
www.cedarhollowhomesx.com

```html
<!DOCTYPE html>
<html lang="en">
<head>
<meta charset="utf-8">
<title>Cedar Hollow at Pine Basin – Marketing Sign</title>
<link rel="stylesheet" href="https://fonts.googleapis.com/css2?family=Josefin+Sans:wght@400&family=Kaushan+Script&family=Tinos:wght@400;700&display=swap">
<style>
  :root {
    --page-bg: #ececec;
    --sky-top: #cfe0f3;
    --sign-white: #ffffff;
    --brand-teal: #1b9bb5;
    --headline-blue: #1f5ea8;
    --tagline-blue: #1c4f9c;
    --band-teal: #1a93b3;
    --band-text: #ffffff;
  }
  * { margin: 0; padding: 0; box-sizing: border-box; }
  html, body {
    width: 800px; height: 1200px; overflow: hidden;
    background: var(--page-bg);
  }
  .sign {
    position: absolute; left: 131px; top: 62px;
    width: 538px; height: 1076px;
    background: linear-gradient(to bottom, var(--sky-top) 0%, var(--sign-white) 22%, var(--sign-white) 100%);
    overflow: hidden;
  }
  .brand {
    position: absolute; left: 0; right: 0; top: 36px;
    text-align: center;
  }
  .brand-square {
    display: block; width: 62px; height: 62px; margin: 0 auto 22px;
    border: 3px solid var(--brand-teal);
  }
  .brand-name {
    font-family: "Josefin Sans", sans-serif; font-weight: 400;
    color: var(--brand-teal); line-height: 1.05;
  }
  .brand-name .primary { display: block; font-size: 36px; letter-spacing: 1px; }
  .brand-name .secondary { display: block; font-size: 19px; }
  .tagline {
    position: absolute; left: 0; right: 0; top: 282px;
    text-align: center;
    font-family: "Kaushan Script", cursive;
    font-size: 44px; color: var(--tagline-blue);
  }
  .rendering {
    position: absolute; left: 0; top: 338px; width: 538px; height: 398px;
    background:
      linear-gradient(to bottom, rgba(255,255,255,0) 0%, rgba(255,255,255,0) 85%, #ffffff 100%),
      linear-gradient(to bottom, #dfe9f2 0%, #b9c6b0 30%, #a99b86 52%, #7e7a76 68%, #6f8a5c 86%, #9fb58a 100%);
  }
  .headline {
    position: absolute; left: 0; right: 0; top: 748px;
    text-align: center; color: var(--headline-blue);
    font-family: "Tinos", serif;
  }
  .headline .join { display: block; font-weight: 700; font-size: 39px; line-height: 44px; }
  .headline .today { display: block; font-weight: 700; font-size: 96px; line-height: 88px; }
  .headline .move-in { display: block; font-size: 40px; letter-spacing: 2px; line-height: 52px; margin-top: 4px; }
  .headline .season { display: block; font-size: 36px; line-height: 42px; }
  .web-band {
    position: absolute; left: 0; bottom: 0; width: 538px; height: 68px;
    background: var(--band-teal);
    display: flex; align-items: center; justify-content: center; gap: 12px;
    color: var(--band-text);
    font-family: "Tinos", serif; font-weight: 700; font-size: 27px;
  }
  .web-band svg { width: 22px; height: 22px; }
</style>
</head>
<body>
  <div class="sign">
    <div class="brand">
      <span class="brand-square"></span>
      <div class="brand-name">
        <span class="primary">CEDAR HOLLOW</span>
        <span class="secondary">at Pine Basin</span>
      </div>
    </div>

    <div class="tagline">Life outside the lines</div>

    <div class="rendering" role="img" aria-label="Watercolour rendering of three-storey apartment buildings with trees, parking lot and landscaping"></div>

    <div class="headline">
      <span class="join">JOIN OUR WAITLIST</span>
      <span class="today">TODAY!</span>
      <span class="move-in">Move-In Beginning</span>
      <span class="season">Summer 2017</span>
    </div>

    <div class="web-band">
      <svg viewBox="0 0 24 24" fill="none" stroke="currentColor" stroke-width="1.8" aria-hidden="true">
        <circle cx="12" cy="12" r="10"/>
        <ellipse cx="12" cy="12" rx="4.5" ry="10"/>
        <line x1="2" y1="12" x2="22" y2="12"/>
        <path d="M4 6.5h16M4 17.5h16"/>
      </svg>
      <span class="web-address">www.cedarhollowhomesx.com</span>
    </div>
  </div>
</body>
</html>
```